Veltrom Limited Business Card Design Project

Veltrom Limited is my UK based company used as my brand to work as an Interim Manager or contractor in project/programme management and Non-Executive Director.

Veltrom is Latin for 'execute' as in getting things done rather than killing people!

Logo and design needs to promote reliable, professional, and successful project delivery. Simple, elegant, clean, professional are words that should spring to mind!

Target Market(s)

Middle and senior management in english speaking countries aged 35 - 60 that hire and task qualified and experienced project/programme managers and Non-Executive Directors.

Industry/Entity Type

Contractor

Font styles to use
Serif
Sans Serif

Requirements
Must have
• Mobile telephone number 07842 615509
email address peterhollis@veltrom-example.co.uk
Nice to have
• ProfNet link to my profile.

Interim Manager
Should not have
• avoid Ticks and clocks

```html
<!DOCTYPE html>
<html lang="en">
<head>
<meta charset="utf-8">
<title>Veltrom Limited – Business Card</title>
<link rel="stylesheet" href="https://fonts.googleapis.com/css2?family=Lato:wght@400;700;900&display=swap">
<style>
  :root {
    --page: #e6e6e6;
    --card-dark: #363333;
    --card-light: #ffffff;
    --ink: #2b2b2b;
    --muted: #6e6c6c;
    --map-tone: #4a4747;
  }
  * { box-sizing: border-box; margin: 0; padding: 0; }
  html, body { width: 1000px; height: 1200px; overflow: hidden; }
  body {
    background: var(--page);
    font-family: "Lato", "Helvetica Neue", Arial, sans-serif;
    color: var(--ink);
    position: relative;
  }
  .card {
    position: absolute;
    left: 70px;
    width: 860px;
    height: 500px;
    background: var(--card-dark);
    overflow: hidden;
    box-shadow: 0 2px 8px rgba(0,0,0,0.15);
  }
  .card--front { top: 70px; }
  .card--back { top: 630px; }

  /* Front */
  .brand-band {
    position: absolute;
    left: 0; top: 0;
    width: 350px; height: 500px;
  }
  .brand-vertical {
    position: absolute;
    left: 175px; top: 250px;
    transform: translate(-50%, -50%) rotate(-90deg);
    text-align: center;
    white-space: nowrap;
  }
  .brand-vertical .brand-name {
    font-weight: 900;
    font-size: 40px;
    color: var(--muted);
    line-height: 1;
  }
  .brand-vertical .brand-slogan {
    font-size: 16px;
    letter-spacing: 6px;
    color: var(--muted);
    margin-top: 6px;
  }
  .info-panel {
    position: absolute;
    left: 350px; top: 0;
    width: 510px; height: 500px;
    background: var(--card-light);
  }
  .info-panel .notch {
    position: absolute;
    left: -1px; top: 104px;
    width: 14px; height: 32px;
  }
  .person {
    position: absolute;
    left: 52px; top: 106px;
  }
  .person-name {
    font-size: 27px;
    font-weight: 400;
    line-height: 1;
    letter-spacing: 0.5px;
  }
  .person-name strong { font-weight: 900; }
  .person-role {
    font-size: 14px;
    font-weight: 700;
    margin-top: 4px;
    letter-spacing: 0.3px;
  }
  .company {
    position: absolute;
    left: 52px; top: 235px;
    width: 375px;
    font-size: 27px;
    line-height: 1;
    padding-bottom: 9px;
    border-bottom: 2px solid var(--ink);
  }
  .company strong { font-weight: 900; }
  .contacts {
    position: absolute;
    left: 52px; top: 284px;
    list-style: none;
  }
  .contacts li {
    display: flex;
    align-items: center;
    height: 30.5px;
    font-size: 16px;
  }
  .contacts svg {
    width: 15px; height: 15px;
    margin-right: 14px;
    fill: var(--ink);
  }

  /* Back */
  .map-area {
    position: absolute;
    left: 100px; top: 73px;
    width: 627px; height: 244px;
    background: radial-gradient(ellipse at center, var(--map-tone) 0%, rgba(74,71,71,0.35) 60%, rgba(54,51,51,0) 100%);
  }
  .brand-corner {
    position: absolute;
    right: 72px; top: 372px;
    text-align: center;
  }
  .brand-corner .brand-name {
    font-weight: 900;
    font-size: 38px;
    color: var(--muted);
    line-height: 1;
  }
  .brand-corner .brand-slogan {
    font-size: 16px;
    letter-spacing: 6px;
    color: var(--muted);
    margin-top: 6px;
  }
</style>
</head>
<body>

<section class="card card--front">
  <div class="brand-band">
    <div class="brand-vertical">
      <div class="brand-name">Veltrom</div>
      <div class="brand-slogan">Getting Things Done</div>
    </div>
  </div>

  <div class="info-panel">
    <svg class="notch" viewBox="0 0 14 32" aria-hidden="true">
      <polygon points="0,0 14,16 0,32" fill="var(--card-dark)"/>
    </svg>

    <div class="person">
      <div class="person-name">PETER <strong>HOLLIS</strong></div>
      <div class="person-role">INTERIM MANAGER</div>
    </div>

    <div class="company"><strong>VELTROM</strong> LIMITED</div>

    <ul class="contacts">
      <li>
        <svg viewBox="0 0 16 16" aria-hidden="true"><path d="M2 6c0-2 2.5-3.5 6-3.5S14 4 14 6l-3 .8-.6-1.6H5.6L5 6.8z M4 8h8l1 5H3z"/></svg>
        07842 615509
      </li>
      <li>
        <svg viewBox="0 0 16 16" aria-hidden="true"><path d="M1 3h14v10H1z M2 4.2v.6l6 4 6-4v-.6z" fill-rule="evenodd"/></svg>
        peterhollis@veltrom-example.co.uk
      </li>
      <li>
        <svg viewBox="0 0 16 16" aria-hidden="true"><path d="M6.5 9.5l3-3M7 4.5l1.6-1.6a2.5 2.5 0 013.5 3.5L10.5 8M9 11.5l-1.6 1.6a2.5 2.5 0 01-3.5-3.5L5.5 8" stroke="var(--ink)" stroke-width="1.6" fill="none" stroke-linecap="round"/></svg>
        www.veltrom-example.co.uk
      </li>
      <li>
        <svg viewBox="0 0 16 16" aria-hidden="true"><path d="M8 1.5L0.5 8h2.2v6.5h4v-4h2.6v4h4V8h2.2z"/></svg>
        14 Harlow Lane, Reading RG1 4QT
      </li>
    </ul>
  </div>
</section>

<section class="card card--back">
  <div class="map-area" role="img" aria-label="Faint dotted world map decoration"></div>
  <div class="brand-corner">
    <div class="brand-name">Veltrom</div>
    <div class="brand-slogan">Getting Things Done</div>
  </div>
</section>

</body>
</html>
```